Wired Earphone Creative Packaging Design

We would like a creative window box style packaging design for our wired earphone

Size: 6” x 3.5” x 1.5” (enclosed die-cut drawing)
Material: E Flute Paper box
Type: Window Box style
Design features we prefer: friendly, playful, creative, trendy, unique, High tech.
Competitors: Enclosed
Requirement:AI file is preferred

Enclosed are product pictures, marketing materials and competitor designs for your reference.

Any further questions, please feel free to ask.
Updates

So designers get more time to design

Target Market(s)

13-40 Year Olds

Industry/Entity Type

Audio

Colors

Designer to choose colors to be used in the design.

Requirements
Must have
• Window, selling point, creative

```html
<!DOCTYPE html>
<html lang="en">
<head>
<meta charset="utf-8">
<title>KT-7 Earphone Window Box</title>
<link rel="stylesheet" href="https://fonts.googleapis.com/css2?family=Abril+Fatface&family=Open+Sans:wght@400;600;700&display=swap">
<style>
  :root {
    --deep-blue: #0070b8;
    --sky-blue: #1fa8e6;
    --pale-blue: #e0f3fc;
    --light-blue: #85d3f5;
    --olive: #a29c00;
    --purple: #8b2a8f;
    --green: #109a4b;
    --cream: #fef9d6;
    --orange: #f7b36b;
    --panel-grey: #ececec;
    --ink: #222;
    --bullet: #1fa8e6;
  }
  html, body { margin: 0; padding: 0; overflow: hidden; background: #fff; }
  .dieline { display: block; width: 1200px; height: 1200px; }
  .title-serif { font-family: "Abril Fatface", "Times New Roman", serif; }
  .body-sans { font-family: "Open Sans", Arial, sans-serif; }
  .pill-text { font-family: "Open Sans", Arial, sans-serif; font-weight: 700; fill: #fff; }
  .list-text { font-family: "Open Sans", Arial, sans-serif; font-size: 22px; fill: var(--ink); }
  .bullet { fill: var(--bullet); }
</style>
</head>
<body>
<svg class="dieline" viewBox="0 0 1500 1500" xmlns="http://www.w3.org/2000/svg">
  <defs>
    <linearGradient id="spineFade" x1="0" y1="0" x2="0" y2="1">
      <stop offset="0" stop-color="#ececec"/>
      <stop offset="0.6" stop-color="#ffffff"/>
    </linearGradient>
    <linearGradient id="productTone" x1="0" y1="0" x2="1" y2="1">
      <stop offset="0" stop-color="#ffffff"/>
      <stop offset="0.7" stop-color="#d9d9d9"/>
      <stop offset="1" stop-color="#e9c15a"/>
    </linearGradient>
  </defs>

  <!-- FRONT PANEL -->
  <g class="front-panel">
    <rect x="37" y="158" width="583" height="999" fill="#fff"/>
    <path d="M37 158 H620 V222 Q330 172 37 240 Z" fill="var(--deep-blue)"/>
    <path d="M37 240 Q330 172 620 222 V236 Q330 192 37 252 Z" fill="var(--sky-blue)"/>
    <path d="M620 158 H737 Q660 250 560 298 L510 313 H620 Z" fill="var(--deep-blue)"/>
    <path d="M510 313 Q640 270 737 158" fill="none" stroke="#111" stroke-width="5"/>
    <text class="title-serif" x="329" y="263" text-anchor="middle" font-size="40" fill="var(--purple)" textLength="488" lengthAdjust="spacingAndGlyphs">Customizable Stereo In-Ear Earphones</text>
    <rect x="37" y="285" width="500" height="7" fill="var(--olive)"/>
    <rect x="222" y="276" width="224" height="24" rx="12" fill="var(--olive)"/>
    <text class="pill-text" x="334" y="295" text-anchor="middle" font-size="18">Model Number: KT-7</text>

    <path d="M205 1065 L345 870 Q410 800 470 855 L620 945 V1065 Z" fill="var(--pale-blue)"/>
    <text class="body-sans" x="348" y="907" font-size="26" font-weight="600" fill="var(--purple)">Features:</text>
    <g class="feature-list">
      <circle class="bullet" cx="338" cy="929" r="6"/><text class="list-text" x="355" y="937">Customizable earbuds</text>
      <circle class="bullet" cx="338" cy="957" r="6"/><text class="list-text" x="355" y="965">In Line Mic</text>
      <circle class="bullet" cx="338" cy="985" r="6"/><text class="list-text" x="355" y="993">Silicone Gel Ear tips</text>
      <circle class="bullet" cx="338" cy="1013" r="6"/><text class="list-text" x="355" y="1021">3.5mm Jack</text>
      <circle class="bullet" cx="338" cy="1042" r="6"/><text class="list-text" x="355" y="1050">Ergonomic Design</text>
    </g>
    <rect x="37" y="1065" width="583" height="92" fill="var(--cream)"/>
    <rect x="37" y="1062" width="583" height="6" fill="var(--orange)"/>
    <text class="body-sans" x="328" y="1095" text-anchor="middle" font-size="20" fill="var(--ink)">The window in front should show below actual product</text>
    <text class="body-sans" x="328" y="1119" text-anchor="middle" font-size="20" fill="var(--ink)">Earbuds, Controller, Jack, 4 Customizable caps</text>
  </g>

  <!-- SPINE -->
  <g class="spine-panel">
    <path d="M737 158 H868 V1157 H620 V313 L620 300 Q690 240 737 158 Z" fill="url(#spineFade)"/>
    <path d="M620 958 L985 1157 H620 Z" fill="var(--light-blue)"/>
    <rect x="685" y="230" width="80" height="90" rx="30" fill="url(#productTone)" role="img" aria-label="Earbud product render"/>
    <rect x="755" y="355" width="70" height="95" rx="28" fill="url(#productTone)" role="img" aria-label="Earbud product render"/>
    <rect x="763" y="400" width="8" height="572" fill="var(--olive)"/>
    <rect x="755" y="562" width="24" height="222" rx="12" fill="var(--olive)"/>
    <text class="pill-text" transform="translate(774 673) rotate(-90)" text-anchor="middle" font-size="18">Model Number: KT-7</text>
    <text class="title-serif" transform="translate(735 672) rotate(-90)" text-anchor="middle" font-size="42" fill="var(--green)" textLength="620" lengthAdjust="spacingAndGlyphs">Customizable Stereo In- Ear Earphones</text>
  </g>

  <!-- BACK PANEL -->
  <g class="back-panel">
    <rect x="868" y="158" width="584" height="999" fill="var(--panel-grey)"/>
    <path d="M1380 232 C1420 280 1340 340 1380 420 C1420 500 1400 560 1420 640 C1440 720 1400 800 1430 900 C1460 1000 1200 1100 1060 1157 H1452 V232 Z" fill="var(--cream)"/>
    <path d="M1380 232 C1420 280 1340 340 1380 420 C1420 500 1400 560 1420 640 C1440 720 1400 800 1430 900 C1460 1000 1200 1100 1060 1157" fill="none" stroke="var(--orange)" stroke-width="10"/>
    <path d="M868 158 H1452 V248 Q1150 150 868 250 Z" fill="var(--deep-blue)"/>
    <path d="M868 250 Q1150 150 1452 248 V264 Q1150 172 868 266 Z" fill="var(--sky-blue)"/>

    <rect x="955" y="283" width="155" height="97" rx="40" fill="url(#productTone)" role="img" aria-label="Pair of earbuds"/>
    <rect x="1180" y="283" width="155" height="92" rx="40" fill="url(#productTone)" role="img" aria-label="Pair of earbuds"/>
    <rect x="1225" y="405" width="165" height="260" rx="12" fill="url(#productTone)" role="img" aria-label="In-line controller front view"/>
    <rect x="910" y="595" width="300" height="200" rx="30" fill="url(#productTone)" role="img" aria-label="In-line controller with clip"/>
    <rect x="925" y="968" width="125" height="112" rx="36" fill="url(#productTone)" role="img" aria-label="Earbud with cap"/>
    <rect x="1110" y="968" width="130" height="112" rx="36" fill="url(#productTone)" role="img" aria-label="Earbud with cap"/>

    <path d="M868 411 H1010 A14 14 0 0 1 1010 439 H868 Z" fill="var(--olive)"/>
    <text class="pill-text" x="958" y="433" text-anchor="middle" font-size="21">Contents</text>
    <g class="contents-list">
      <circle class="bullet" cx="925" cy="458" r="5"/><text class="list-text" x="939" y="468">2 Pairs of Switchable Caps</text>
      <circle class="bullet" cx="925" cy="491" r="5"/><text class="list-text" x="939" y="501">3 Pairs of Silicone Ear tips</text>
      <circle class="bullet" cx="925" cy="524" r="5"/><text class="list-text" x="939" y="534">User Manual</text>
    </g>

    <path d="M1452 773 H1257 A14 14 0 0 0 1257 802 H1452 Z" fill="var(--olive)"/>
    <text class="pill-text" x="1332" y="796" text-anchor="middle" font-size="21">Specification:</text>
    <g class="spec-list" text-anchor="end">
      <text class="list-text" x="1371" y="842">Frequency Response: 20-20KHz</text><circle class="bullet" cx="1382" cy="834" r="5"/>
      <text class="list-text" x="1371" y="875">Sensitivity: 105±3dB</text><circle class="bullet" cx="1382" cy="867" r="5"/>
      <text class="list-text" x="1365" y="908">THD: &lt;3%</text><circle class="bullet" cx="1382" cy="900" r="5"/>
      <text class="list-text" x="1371" y="941">Cord Length: 3.6ft</text><circle class="bullet" cx="1382" cy="933" r="5"/>
    </g>
  </g>

  <path class="feature-arc" d="M205 1065 L345 870 Q410 800 470 855 L985 1157" fill="none" stroke="var(--deep-blue)" stroke-width="14"/>
</svg>
</body>
</html>
```